App Design Project

We had an vantrix/norvel app built (freelancer), without any real design applied. Currently just made up of plain buttons and text. No colors, images, etc.
App is about 20 total pages, and contains a login window, a main menu, and then several different options that pull data via web services from our back-end.
About the app:
The application will be used by physicians, who are in essence speakers who are speaking on behalf of pharmaceutical companies, to train doctors on the use of their products. They will use the app to get a list of their upcoming speaking engagements, calendars, access to slide presentations, and the ability for them to submit expense forms with pictures of receipts, etc.
We need the following things:
* An App Icon
* An Vantrix startup screen
* Two Norvel startup screens (one portrait and one landscape)
* Color schedme recommendations for the pages
* Page design recommendations: header/footer
The Vantrix and Norvel startup screens are screens displayed while the app is loading (splash screen). They are simply a large version of the app's logo (with differing dimensions) and maybe some extra detail as the space allows more. The Norvel and Vantrix screens can be identical, but please note the size. orientation and aspect ratio differences.
Objects possibilities...(pick any/none/anything else that is appropriate):
* Person behind a podium
* Someone speaking / presenting
* be creative
Styles we like:
This is for pharma, so medical might be appropriate
open to recommendations
Keep in mind that we are looking for page design recommendations as well. We could provide sample screens with text, and then are looking for recommendations on color, and general page design.
A successful designer may also win several other apps currently under consideration.
Reason: Added a document on 8/13 with additional details to help designers.

```html
<!DOCTYPE html>
<html lang="en">
<head>
<meta charset="utf-8">
<title>Speaker Resource Center — Splash</title>
<link href="https://fonts.googleapis.com/css2?family=Open+Sans:ital,wght@0,400;1,800&display=swap" rel="stylesheet">
<style>
  :root {
    --sky-light: #8eeaff;
    --sky-mid: #4fd0fb;
    --sky-deep: #1fa8ef;
    --ink: #3a3d44;
    --ink-logo: #4a4f59;
    --accent: #f39a2b;
    --streak: rgba(255, 255, 255, 0.18);
  }
  * { margin: 0; padding: 0; box-sizing: border-box; }
  html, body { width: 928px; height: 1200px; overflow: hidden; }
  body {
    position: relative;
    background: radial-gradient(ellipse 75% 60% at 50% 46%, var(--sky-light) 0%, var(--sky-mid) 50%, var(--sky-deep) 100%);
    font-family: "Open Sans", Arial, sans-serif;
  }
  .backdrop-curves {
    position: absolute;
    inset: 0;
    width: 928px;
    height: 1200px;
  }
  .brand-name {
    position: absolute;
    top: 230px;
    left: 0;
    width: 100%;
    text-align: center;
    font-weight: 400;
    font-size: 170px;
    line-height: 1;
    letter-spacing: 2px;
    color: var(--ink-logo);
  }
  .splash-title {
    position: absolute;
    top: 505px;
    left: 0;
    width: 100%;
    text-align: center;
    font-weight: 800;
    font-style: italic;
    font-size: 104px;
    line-height: 96px;
    text-transform: uppercase;
    color: var(--ink);
  }
  .splash-title .highlight { color: var(--accent); display: block; }
  .splash-title span { display: block; }
</style>
</head>
<body>
  <svg class="backdrop-curves" viewBox="0 0 928 1200" aria-hidden="true">
    <path d="M0 180 C 300 260, 620 520, 928 900 L 928 780 C 640 470, 320 220, 0 120 Z" fill="var(--streak)"/>
    <path d="M520 0 C 640 220, 780 380, 928 470 L 928 360 C 800 280, 690 150, 620 0 Z" fill="var(--streak)"/>
    <path d="M0 1000 C 260 900, 560 880, 928 1020 L 928 1200 L 0 1200 Z" fill="rgba(255,255,255,0.08)"/>
  </svg>

  <div class="brand-name">RVN</div>

  <h1 class="splash-title">
    <span>Speaker</span>
    <span class="highlight">Resource</span>
    <span>Center</span>
  </h1>
</body>
</html>
```